Brand-new Pediatric Dental Practice needs a website

We are a brand-new dental practice that will specialize in treating children. We want a gorgeous and easily navigable dental practice website that would make a good first impression to potential patients and their parents. It should be modern, SEO-friendly, mobile responsive, and optimized to win new patients.

Target Market(s)

Parents

Industry/Entity Type

Healthcare/Dentistry

Coding

Coded - Design and coding required

Number of Pages Required

4 page

Requirements
Must have
• Use the Wix website building platform. 4 pages: home, meet our dentists, services, contact us
Nice to have
• has a link to our facebook, instagram

```html
<!DOCTYPE html>
<html lang="en">
<head>
<meta charset="utf-8">
<title>fern hollow pediatric dentistry</title>
<link href="https://fonts.googleapis.com/css2?family=Hind:wght@300;400;500;600;700&family=Montserrat:wght@300;400;600;700&family=Raleway:wght@200;800&display=swap" rel="stylesheet">
<style>
:root{
  --green:#05ad7f;
  --green-dark:#049670;
  --navy:#1c3c8f;
  --ink:#333b45;
  --muted:#7d8790;
  --card:#e9eef3;
  --footer:#e4e9ef;
  --white:#ffffff;
}
*{margin:0;padding:0;box-sizing:border-box}
html,body{width:1200px;height:4950px;overflow:hidden}
body{position:relative;background:var(--white);font-family:'Hind',sans-serif;color:var(--ink)}
.abs{position:absolute}
.header{left:0;top:0;width:1200px;height:125px;background:var(--green)}
.logo-badge{left:45px;top:-70px;width:200px;height:200px;border-radius:50%;background:var(--white)}
.logo-mark{left:117px;top:10px;width:56px;height:56px;border-radius:50%;background:var(--green)}
.logo-name{left:45px;top:66px;width:200px;text-align:center;font:500 28px 'Hind',sans-serif;color:#3b4a4a;line-height:1}
.logo-sub{left:45px;top:98px;width:200px;text-align:center;font:500 9px 'Montserrat',sans-serif;letter-spacing:2px;color:var(--green)}
.nav{right:54px;top:55px;display:flex;gap:38px;font:400 15px 'Montserrat',sans-serif;color:var(--white)}
.hero{left:0;top:125px;width:1200px;height:831px;background:linear-gradient(120deg,#e9d8cc 0%,#d9a088 35%,#b8d3dc 70%,#e7f0f2 100%)}
.hero-title{right:33px;top:282px;text-align:right;font:200 70px 'Raleway',sans-serif;color:var(--green);line-height:1}
.hero-title2{right:33px;top:360px;font:800 66px 'Raleway',sans-serif;color:var(--green);line-height:1}
.hero-text{right:33px;top:460px;width:590px;text-align:right;font:700 14px 'Montserrat',sans-serif;color:var(--white);line-height:17px;text-transform:uppercase}
.btn{display:flex;align-items:center;justify-content:center;font:700 14px 'Montserrat',sans-serif;border-radius:4px;box-shadow:0 4px 10px rgba(0,0,0,.2)}
.btn-light{left:648px;top:633px;width:212px;height:59px;background:var(--white);color:var(--green)}
.btn-green{left:910px;top:633px;width:215px;height:59px;background:var(--green);color:var(--white)}
.service{width:280px;height:90px}
.service-icon{left:0;top:0;width:77px;height:77px}
.service h3{position:absolute;left:92px;top:2px;font:400 21px 'Hind',sans-serif;color:var(--ink)}
.service p{position:absolute;left:92px;top:34px;width:180px;font:400 13px/22px 'Hind',sans-serif;color:var(--muted)}
.quote{left:0;top:1327px;width:575px;height:586px;background:var(--green)}
.quote-photo{left:575px;top:1381px;width:625px;height:480px;background:linear-gradient(135deg,#d9dfe6,#4fd08c 55%,#2a4fa8)}
.quote h2{position:absolute;left:48px;top:56px;font:400 34px 'Hind',sans-serif;color:var(--white)}
.quote h2 b{font-weight:700}
.quote p{position:absolute;left:48px;top:122px;width:480px;font:400 14px/23px 'Hind',sans-serif;color:var(--white)}
.field{background:var(--white);font:400 13px 'Hind',sans-serif;color:#aab;padding:14px 22px}
.quote-btn{left:48px;top:469px;width:146px;height:46px;background:var(--navy);color:var(--white);font:500 12px 'Hind',sans-serif;display:flex;align-items:center;justify-content:center}
.eyebrow{font:400 21px 'Hind',sans-serif;color:var(--navy)}
.section-title{font:700 36px/1 'Hind',sans-serif;color:var(--navy)}
.pill-btn{left:979px;top:2031px;width:173px;height:48px;background:var(--green);color:var(--white);font:500 12px 'Hind',sans-serif;display:flex;align-items:center;justify-content:center}
.review{top:2142px;width:266px;height:273px;background:var(--card)}
.review h4{position:absolute;left:38px;top:38px;font:700 23px/24px 'Hind',sans-serif;color:var(--green)}
.review .role{position:absolute;left:38px;top:88px;width:120px;font:400 14px/22px 'Hind',sans-serif;color:var(--ink)}
.review .avatar{position:absolute;right:38px;top:60px;width:36px;height:36px;border-radius:50%;background:#c49a86}
.review .body{position:absolute;left:38px;width:200px;font:400 14px/23px 'Hind',sans-serif;color:var(--ink)}
.dots{left:544px;top:2455px;display:flex;gap:10px;align-items:center}
.dots i{display:block;width:12px;height:2px;background:#cdd}
.dots i.on{width:14px;height:14px;border-radius:50%;background:var(--green)}
.pro-photo{left:0;top:2571px;width:600px;height:616px;background:linear-gradient(135deg,#3fcf8a,#e9e5df 45%,#c89a86 70%,#cfe7e8)}
.small-caps{font:400 12px/15px 'Montserrat',sans-serif;font-variant:small-caps;color:var(--ink)}
.member{top:2952px;width:180px;height:100px;background:var(--card)}
.member span{position:absolute;left:50px;top:30px;width:80px;height:40px;border-radius:6px;background:#bfe6d6}
.doc{top:3227px;width:354px;height:652px;background:var(--card)}
.doc .photo{position:absolute;left:0;top:0;width:354px;height:354px}
.doc .role{position:absolute;left:29px;top:395px;font:400 14px 'Hind',sans-serif;color:var(--ink)}
.doc h4{position:absolute;left:29px;top:424px;font:300 28px 'Hind',sans-serif;color:var(--navy)}
.doc h4 b{font-weight:600}
.doc p{position:absolute;left:29px;top:484px;width:300px;font:400 14px/23px 'Hind',sans-serif;color:var(--ink)}
.doc .more{position:absolute;left:29px;width:109px;height:48px;background:var(--white);color:var(--green);font:400 12px 'Hind',sans-serif;display:flex;align-items:center;justify-content:center;box-shadow:0 2px 5px rgba(0,0,0,.12)}
.doc .socials{position:absolute;right:29px;display:flex;gap:12px}
.doc .socials i{display:block;width:10px;height:10px;border-radius:50%;background:var(--navy)}
.bar-label{font:400 14px 'Hind',sans-serif;color:var(--ink)}
.bar{width:552px;height:8px;background:#e3e8ec;border-radius:4px}
.bar span{display:block;height:8px;background:var(--green);border-radius:4px}
.smile-photo{left:619px;top:3998px;width:552px;height:425px;background:linear-gradient(90deg,#e8c6b6,#b53a42 45%,#f4eee6 60%,#c99684)}
.footer{left:0;top:4550px;width:1200px;height:319px;background:var(--footer)}
.footer-text{left:29px;top:4694px;width:250px;font:400 14px/29px 'Hind',sans-serif;color:var(--ink)}
.footer-nav{left:363px;top:4648px;font:400 13px/32px 'Montserrat',sans-serif;color:#8a96a2}
.footer h5{position:absolute;top:4648px;font:400 24px 'Hind',sans-serif;color:var(--green)}
.award{top:4704px;width:62px;height:62px;border-radius:50%;border:3px solid #b9c2cb;background:#d7dde3}
.social{top:4730px;width:36px;height:36px;border-radius:50%;background:var(--navy)}
.bottom{left:0;top:4869px;width:1200px;height:81px;background:var(--green);display:flex;justify-content:center;align-items:center;gap:22px;font:400 13px 'Montserrat',sans-serif;color:var(--white)}
</style>
</head>
<body>

<header class="abs header">
  <div class="abs logo-badge"></div>
  <div class="abs logo-mark"></div>
  <div class="abs logo-name">fern hollow</div>
  <div class="abs logo-sub">PEDIATRIC DENTISTRY</div>
  <nav class="abs nav"><span>HOME</span><span>MEET OUR DENTISTS</span><span>SERVICES</span><span>CONTACT US</span></nav>
</header>

<section class="abs hero" role="img" aria-label="Smiling patient during a dental check-up with a mirror"></section>
<h1 class="abs hero-title">AWESOM SMILES</h1>
<div class="abs hero-title2">GREAT CARE</div>
<p class="abs hero-text">Lorem ipsum dolor sit amet, consectetur adipiscing elit, sed do eiusmod tempor incididunt ut labore et dolore magna aliqua. Quis ipsum suspendisse ultrices gravida. Risus commodo viverra maecenas accumsan lacus vel facilisis.</p>
<div class="abs btn btn-light">VIEW OUR PORTFOLIO</div>
<div class="abs btn btn-green">VIEW OUR PORTFOLIO</div>

<section class="services">
  <div class="abs service" style="left:29px;top:1018px"><svg class="abs service-icon" viewBox="0 0 77 77"><circle cx="38.5" cy="38.5" r="37" fill="none" stroke="#05ad7f" stroke-width="2"/><circle cx="38.5" cy="38.5" r="10" fill="none" stroke="#05ad7f" stroke-width="2"/></svg><h3>General Dentistry</h3><p>Competently parallel task researched data process.</p></div>
  <div class="abs service" style="left:319px;top:1018px"><svg class="abs service-icon" viewBox="0 0 77 77"><circle cx="38.5" cy="38.5" r="37" fill="none" stroke="#1c3c8f" stroke-width="2"/><circle cx="38.5" cy="38.5" r="10" fill="none" stroke="#1c3c8f" stroke-width="2"/></svg><h3>Implants</h3><p>Leverage other resource leveling convergence data.</p></div>
  <div class="abs service" style="left:610px;top:1018px"><svg class="abs service-icon" viewBox="0 0 77 77"><circle cx="38.5" cy="38.5" r="37" fill="none" stroke="#05ad7f" stroke-width="2"/><circle cx="38.5" cy="38.5" r="10" fill="none" stroke="#05ad7f" stroke-width="2"/></svg><h3>Dental Surgery</h3><p>Engage fully tested process top line platform clients.</p></div>
  <div class="abs service" style="left:900px;top:1018px"><svg class="abs service-icon" viewBox="0 0 77 77"><circle cx="38.5" cy="38.5" r="37" fill="none" stroke="#1c3c8f" stroke-width="2"/><circle cx="38.5" cy="38.5" r="10" fill="none" stroke="#1c3c8f" stroke-width="2"/></svg><h3>Alignment</h3><p>User generated content in real time offshoring.</p></div>
  <div class="abs service" style="left:29px;top:1154px"><svg class="abs service-icon" viewBox="0 0 77 77"><circle cx="38.5" cy="38.5" r="37" fill="none" stroke="#05ad7f" stroke-width="2"/><circle cx="38.5" cy="38.5" r="10" fill="none" stroke="#05ad7f" stroke-width="2"/></svg><h3>Teeth Braces</h3><p>Synthesize integrated schemas with networks.</p></div>
  <div class="abs service" style="left:319px;top:1154px"><svg class="abs service-icon" viewBox="0 0 77 77"><circle cx="38.5" cy="38.5" r="37" fill="none" stroke="#1c3c8f" stroke-width="2"/><circle cx="38.5" cy="38.5" r="10" fill="none" stroke="#1c3c8f" stroke-width="2"/></svg><h3>Whitening</h3><p>Incubate standards great channels scalable benefits.</p></div>
  <div class="abs service" style="left:610px;top:1154px"><svg class="abs service-icon" viewBox="0 0 77 77"><circle cx="38.5" cy="38.5" r="37" fill="none" stroke="#05ad7f" stroke-width="2"/><circle cx="38.5" cy="38.5" r="10" fill="none" stroke="#05ad7f" stroke-width="2"/></svg><h3>Teeth Protection</h3><p>Evisculate holistic innovation rather than centric data.</p></div>
  <div class="abs service" style="left:900px;top:1154px"><svg class="abs service-icon" viewBox="0 0 77 77"><circle cx="38.5" cy="38.5" r="37" fill="none" stroke="#1c3c8f" stroke-width="2"/><circle cx="38.5" cy="38.5" r="10" fill="none" stroke="#1c3c8f" stroke-width="2"/></svg><h3>Prosthesis</h3><p>Revolutionize global sources through dental services.</p></div>
</section>

<div class="abs quote-photo" role="img" aria-label="Dentist in green scrubs holding an apple and a dental mirror"></div>
<section class="abs quote">
  <h2>Get A <b>Free Quote</b></h2>
  <p>Leverage agile frameworks to provide a robust synopsis for high level overviews. Iterative approaches to corporate strategy foster collaborative thinking to further the overall value proposition.</p>
  <div class="abs field" style="left:48px;top:223px;width:233px;height:46px">Your name *</div>
  <div class="abs field" style="left:294px;top:223px;width:233px;height:46px">Your Email Address *</div>
  <div class="abs field" style="left:48px;top:292px;width:479px;height:148px">Message and dental procedure you need *</div>
  <div class="abs quote-btn" style="top:469px">Get A Quote Now</div>
</section>

<div class="abs eyebrow" style="left:29px;top:2010px">Clients With</div>
<h2 class="abs section-title" style="left:29px;top:2040px">Reason To Smile</h2>
<div class="abs pill-btn">All Client Testimonials</div>

<article class="abs review" style="left:21px"><h4>Nora<br>Bell</h4><div class="avatar" role="img" aria-label="Client portrait"></div><div class="role">Full Dental Implants</div><p class="body" style="top:152px">Capitalize on low hanging fruit to identify a ballpark value added activity to beta test clickthroughs from users.</p></article>
<article class="abs review" style="left:325px"><h4>Lena<br>Park</h4><div class="avatar" role="img" aria-label="Client portrait"></div><div class="role">Cosmetic Dentistry</div><p class="body" style="top:152px">Collaboratively administrate empowered markets via plug-and-play networks after installed base benefits.</p></article>
<article class="abs review" style="left:631px;height:250px"><h4>Owen Reed</h4><div class="avatar" role="img" aria-label="Client portrait" style="top:38px;background:#8a5a44"></div><div class="role" style="top:64px">Dental surgery</div><p class="body" style="top:105px">Holisticly predominate extensible testing procedures for reliable supply chains top line service cutting edge deliverables.</p></article>
<article class="abs review" style="left:935px"><h4>Clara<br>Wynn</h4><div class="avatar" role="img" aria-label="Client portrait"></div><div class="role" style="width:150px">Teeth Whitening</div><p class="body" style="top:128px">Distinctively exploit optimal alignments for intuitive bandwidth. Quickly coordinate e-business applications.</p></article>
<div class="abs dots"><i></i><i class="on"></i><i></i><i></i><i></i><i></i></div>

<div class="abs pro-photo" role="img" aria-label="Dentist examining a smiling patient in the dental chair"></div>
<div class="abs eyebrow" style="left:638px;top:2707px">The Dental</div>
<h2 class="abs section-title" style="left:638px;top:2733px">Professionals</h2>
<p class="abs small-caps" style="left:642px;top:2778px;width:540px">Lorem ipsum dolor sit amet, consectetur adipiscing elit, sed do eiusmod tempor incididunt ut labore et dolore magna aliqua. Quis ipsum suspendisse ultrices gravida. Risus commodo viverra maecenas accumsan lacus vel facilisis.</p>
<div class="abs" style="left:638px;top:2881px;width:562px;height:1px;background:#dde3e8"></div>
<div class="abs" style="left:638px;top:2903px;font:400 28px 'Hind',sans-serif;color:var(--ink)">Proud Members</div>
<div class="abs member" style="left:638px"><span></span></div>
<div class="abs member" style="left:829px"><span></span></div>
<div class="abs member" style="left:1019px"><span></span></div>

<article class="abs doc" style="left:29px"><div class="photo" role="img" aria-label="Clinic director in green scrubs, arms crossed" style="background:linear-gradient(160deg,#d6dde2,#4fd08c 70%)"></div><div class="role">Clinic Director</div><h4>Adam <b>Hale</b></h4><p>The qualities of excellent communication and trust form part of our commitment to you and I have carefully chosen a great team of people.</p><div class="more" style="top:571px">Read More</div><div class="socials" style="top:590px"><i></i><i></i><i></i><i></i></div></article>
<article class="abs doc" style="left:423px"><div class="photo" role="img" aria-label="Senior dental surgeon in green scrubs" style="background:linear-gradient(160deg,#eef1f3,#4fd08c 70%)"></div><div class="role">Senior Dental Surgeon</div><h4>Victor <b>Sloane</b></h4><p>Committed to delivering dentistry of the highest quality, Victor achieved numerous awards over Europe and United States.</p><div class="more" style="top:571px">Read More</div><div class="socials" style="top:590px"><i></i><i></i><i></i></div></article>
<article class="abs doc" style="left:817px;height:675px"><div class="photo" role="img" aria-label="Senior orthodontist in green scrubs" style="background:linear-gradient(160deg,#f1f2f3,#4fd08c 70%)"></div><div class="role">Senior Orthodontist</div><h4>Rosa <b>Linden</b></h4><p>Emphatic and enjoying treating a wide range of patients, including children, oral hygiene and education is important to me as to my patients.</p><div class="more" style="top:594px">Read More</div><div class="socials" style="top:613px"><i></i><i></i><i></i></div></article>

<div class="abs eyebrow" style="left:29px;top:4052px">Perfect Smile,</div>
<h2 class="abs section-title" style="left:29px;top:4078px">Excellence Defined</h2>
<p class="abs small-caps" style="left:33px;top:4122px;width:440px">Lorem ipsum dolor sit amet, consectetur adipiscing elit, sed do eiusmod tempor incididunt ut labore et dolore magna aliqua. Quis ipsum suspendisse ultrices gravida. Risus commodo viverra maecenas accumsan lacus vel facilisis.</p>
<div class="abs bar-label" style="left:29px;top:4233px">Dental Satisfaction</div>
<div class="abs bar" style="left:29px;top:4259px"><span style="width:96%"></span></div>
<div class="abs bar-label" style="left:29px;top:4286px">Success Rate</div>
<div class="abs bar" style="left:29px;top:4311px"><span style="width:92%"></span></div>
<div class="abs smile-photo" role="img" aria-label="Close-up of a smile comparing teeth before and after whitening"></div>
<svg class="abs" style="left:619px;top:3998px" width="552" height="425" viewBox="0 0 552 425"><line x1="240" y1="0" x2="240" y2="425" stroke="#ffffff" stroke-width="2" opacity=".7"/><circle cx="240" cy="220" r="11" fill="#05ad7f"/></svg>

<footer class="abs footer"></footer>
<div class="abs" style="left:97px;top:4577px;width:52px;height:52px;border-radius:50%;background:var(--green)"></div>
<div class="abs" style="left:40px;top:4633px;font:500 28px/1 'Hind',sans-serif;color:#3b4a4a">fern hollow</div>
<div class="abs" style="left:52px;top:4664px;font:500 9px 'Montserrat',sans-serif;letter-spacing:2px;color:var(--green)">PEDIATRIC DENTISTRY</div>
<p class="abs footer-text">We are a friendly team of dentists working together to ensure that you receive the best treatment that you require.</p>
<div class="abs footer-nav">HOME<br>MEET OUR DENTISTS<br>SERVICES<br>CONTACT US</div>
<h5 class="abs" style="left:629px;top:4642px;font:400 24px 'Hind',sans-serif;color:var(--green)">Our Awards</h5>
<div class="abs award" style="left:629px"></div>
<div class="abs award" style="left:714px"></div>
<div class="abs award" style="left:800px"></div>
<h5 class="abs" style="left:929px;top:4642px;font:400 24px 'Hind',sans-serif;color:var(--green)">Social Networks</h5>
<div class="abs social" style="left:929px"></div>
<div class="abs social" style="left:971px"></div>
<div class="abs social" style="left:1013px"></div>
<div class="abs social" style="left:1055px"></div>

<nav class="abs bottom"><span>HOME</span><span>MEET OUR DENTISTS</span><span>SERVICES</span><span>CONTACT US</span></nav>

</body>
</html>
```